business card and flyer/pricelist

Business Name: Willow Strand Salon
new boutique salon run from home, using Australian owned natural products and colours, we need a flyer design to do a letter box drop to advertise the business as well as incorporating a price list on the front (single sided with writing on front and only colour on back)

The salon has a natural feel with light coloured timber chairs, bamboo timber bench top and shelving.

we are after a natural toned colour for the flyer, with possibly a brown/darkish colour writing

we are after a flyer that will also be able to use the design heading (business name) for business cards as well

feel free to look on my pintrest account to get a feel for my style under Corinne Belvane.

I love simple clean and Natural looks.

Industry/Entity Type

Boutique

Font styles to use
Script
Other font styles liked:
• SCRIPT HANDWRITTEN FONTS

Colors
cadf82
e9f1ce
5c5c5c
d3d3d3
add136
fee18a

Requirements
Must have
• NATURAL COLOURINGS, eg soft greens, browns,
white or off white background.
Should not have
• photos,

```html
<!DOCTYPE html>
<html lang="en">
<head>
<meta charset="utf-8">
<title>Willow Strand Salon – Flyer and Price List</title>
<link rel="stylesheet" href="https://fonts.googleapis.com/css2?family=Open+Sans:wght@400;600;700&family=Sorts+Mill+Goudy&family=Oswald:wght@600&display=swap">
<style>
  :root {
    --page: #ffffff;
    --paper: #f7efc6;
    --paper-light: #faf3d2;
    --gold: #c9a227;
    --gold-deep: #9e7b12;
    --ink: #3d4650;
    --label: #111111;
  }
  * { box-sizing: border-box; margin: 0; padding: 0; }
  html, body { width: 1145px; height: 1200px; overflow: hidden; background: var(--page); }
  body { position: relative; font-family: "Open Sans", Arial, sans-serif; color: var(--ink); }

  .flyer-side {
    position: absolute; top: 59px; width: 489px; height: 1065px;
    background: var(--paper);
  }
  .flyer-front { left: 54px; }
  .flyer-back { left: 594px; }

  .side-label {
    position: absolute; top: 1140px; width: 489px; text-align: center;
    font-family: "Oswald", Impact, sans-serif; font-weight: 600;
    font-size: 36px; color: var(--label); letter-spacing: 1px;
  }
  .side-label.front { left: 54px; }
  .side-label.back { left: 594px; }

  .business-name {
    position: absolute; left: 0; top: 70px; width: 100%;
    text-align: center; font-size: 46px; font-weight: 400;
    color: var(--ink); letter-spacing: 1px;
  }

  .price-list {
    position: absolute; left: 38px; top: 195px; width: 412px; height: 677px;
    padding: 34px 28px 0 28px;
  }
  .price-frame { position: absolute; inset: 0; }
  .price-section { position: relative; margin-bottom: 13px; }
  .price-section h2 {
    font-size: 16px; font-weight: 700; color: var(--gold);
    line-height: 22px; letter-spacing: .3px;
  }
  .price-row {
    display: flex; font-size: 17px; line-height: 21.2px;
  }
  .price-row .service { width: 279px; }
  .price-row .price { color: var(--gold); }

  .offer-box {
    position: absolute; left: 38px; top: 890px; width: 413px; height: 96px;
    border: 2px solid var(--gold); padding: 4px;
  }
  .offer-box-inner {
    height: 100%; border: 2px dotted var(--gold);
    display: flex; flex-direction: column; justify-content: center; align-items: center;
    font-family: "Sorts Mill Goudy", Georgia, serif; font-size: 24px;
    line-height: 30px; color: var(--gold-deep); font-weight: 700;
  }

  .contact {
    position: absolute; left: 0; top: 1001px; width: 100%;
    text-align: center; font-size: 16px; font-weight: 600; line-height: 20px;
    color: var(--ink);
  }
</style>
</head>
<body>

<section class="flyer-side flyer-front" role="img" aria-label="Soft cream honeycomb background pattern">
</section>
<section class="flyer-side flyer-front">
  <h1 class="business-name">Willow Strand Salon</h1>

  <div class="price-list">
    <svg class="price-frame" viewBox="0 0 412 677" width="412" height="677" aria-hidden="true">
      <path d="M16,1.5 H396 A14.5 14.5 0 0 0 410.5,16 V661 A14.5 14.5 0 0 0 396,675.5 H16 A14.5 14.5 0 0 0 1.5,661 V16 A14.5 14.5 0 0 0 16,1.5 Z"
            fill="#faf3d2" stroke="#c9a227" stroke-width="3"/>
      <path d="M19,7 H393 A12 12 0 0 0 405,19 V658 A12 12 0 0 0 393,670 H19 A12 12 0 0 0 7,658 V19 A12 12 0 0 0 19,7 Z"
            fill="none" stroke="#c9a227" stroke-width="1"/>
    </svg>

    <div class="price-section">
      <h2>CUTS</h2>
      <div class="price-row"><span class="service">Ladies (inc. shampoo/blowdry)</span><span class="price">$45</span></div>
      <div class="price-row"><span class="service">Mens</span><span class="price">$20</span></div>
      <div class="price-row"><span class="service">13 &amp; Under</span><span class="price">From $15</span></div>
      <div class="price-row"><span class="service">5 &amp; Under</span><span class="price">$10</span></div>
    </div>
    <div class="price-section">
      <h2>BLOWDRY &amp; STYLING</h2>
      <div class="price-row"><span class="service">Short</span><span class="price">$25</span></div>
      <div class="price-row"><span class="service">Medium</span><span class="price">$30</span></div>
      <div class="price-row"><span class="service">Long</span><span class="price">$40</span></div>
      <div class="price-row"><span class="service">Straight Iron (after blowdry)</span><span class="price">$10</span></div>
      <div class="price-row"><span class="service">Upstyles</span><span class="price">From $60</span></div>
      <div class="price-row"><span class="service">Onsite styling</span><span class="price">POA</span></div>
    </div>
    <div class="price-section">
      <h2>COLOURS</h2>
      <div class="price-row"><span class="service">Regrowth</span><span class="price">$55</span></div>
      <div class="price-row"><span class="service">Short</span><span class="price">$60</span></div>
      <div class="price-row"><span class="service">Medium</span><span class="price">$75</span></div>
      <div class="price-row"><span class="service">Long</span><span class="price">$85</span></div>
    </div>
    <div class="price-section">
      <h2>FOILS</h2>
      <div class="price-row"><span class="service">Top Foils</span><span class="price">$50</span></div>
      <div class="price-row"><span class="service">½ head</span><span class="price">$95</span></div>
      <div class="price-row"><span class="service">¾ head</span><span class="price">$110</span></div>
      <div class="price-row"><span class="service">Full head</span><span class="price">$145</span></div>
      <div class="price-row"><span class="service">(all include toner)</span></div>
    </div>
    <div class="price-section">
      <h2>TREATMENTS</h2>
      <div class="price-row"><span class="service">At basin</span><span class="price">$10</span></div>
      <div class="price-row"><span class="service">Special Feel</span><span class="price">$35</span></div>
      <div class="price-row"><span class="service">Eye brow/lash treatments</span><span class="price">From $10</span></div>
    </div>
  </div>

  <div class="offer-box">
    <div class="offer-box-inner">
      <span>Special introductory offer</span>
      <span>receive 25% off your initial visit</span>
    </div>
  </div>

  <p class="contact">18 Banksia Court Mango Hill<br>0491570156</p>
</section>

<section class="flyer-side flyer-back" role="img" aria-label="Soft cream honeycomb background pattern"></section>

<div class="side-label front">front</div>
<div class="side-label back">back</div>

</body>
</html>
```